Design a (20.4 x 10.14) Banner that says - Keep Hope Rising From Harvest Glow TV Family

We want a design (20.4 x 10.14) with the words 'Keep Hope Rising' as the main text and 'From Harvest Glow TV Family' underneath. For 'Harvest Glow TV', we'd like you to use the logo which can be found in the image attached.

The image attached is just an example but please let your creative juices flow!

Target Market(s)

Christian

Industry/Entity Type

Christian

Requirements
Must have
• Must have the words 'Keep Hope Rising' and 'From Harvest Glow TV Family'.

```html
<!DOCTYPE html>
<html lang="en">
<head>
<meta charset="utf-8">
<title>Keep Hope Rising – Harvest Glow TV Family</title>
<link rel="stylesheet" href="https://fonts.googleapis.com/css2?family=Marcellus&family=Open+Sans:wght@700&display=swap">
<style>
  :root {
    --bg-red: #e5304d;
    --bg-pink: #e4557c;
    --bg-magenta: #c63b78;
    --bg-purple: #9c418b;
    --photo-glow: #f39ab4;
    --title-purple: #8f3a8c;
    --title-pink-light: #f07aa8;
    --title-pink-deep: #b13885;
    --band-black: #000000;
    --band-grey: #3b3b3b;
    --text-white: #ffffff;
  }
  * { margin: 0; padding: 0; box-sizing: border-box; }
  html, body { width: 1200px; height: 604px; overflow: hidden; background: #ffffff; }
  .banner {
    position: relative;
    width: 1200px;
    height: 604px;
    overflow: hidden;
    background: linear-gradient(90deg, var(--bg-red) 0%, var(--bg-red) 22%, var(--bg-pink) 50%, var(--bg-magenta) 72%, var(--bg-purple) 100%);
  }
  .banner__photo {
    position: absolute;
    left: 250px;
    top: -40px;
    width: 640px;
    height: 600px;
    background: radial-gradient(ellipse at 50% 45%, var(--photo-glow) 0%, rgba(243,154,180,0.55) 40%, rgba(243,154,180,0) 72%);
    opacity: 0.8;
  }
  .banner__title {
    position: absolute;
    left: 0;
    right: 0;
    top: 196px;
    display: flex;
    justify-content: center;
    align-items: baseline;
    gap: 34px;
    font-family: "Marcellus", "Optima", serif;
    text-transform: uppercase;
    letter-spacing: 6px;
    line-height: 1;
    text-shadow: 0 3px 8px rgba(90, 20, 70, 0.35);
  }
  .banner__title-word {
    font-size: 86px;
    color: var(--title-purple);
  }
  .banner__title-word--accent {
    font-size: 128px;
    background: linear-gradient(180deg, var(--title-pink-light) 0%, var(--title-pink-deep) 100%);
    -webkit-background-clip: text;
    background-clip: text;
    color: transparent;
    text-shadow: none;
    filter: drop-shadow(0 3px 6px rgba(90, 20, 70, 0.35));
  }
  .banner__wave {
    position: absolute;
    left: 0;
    top: 0;
    width: 1200px;
    height: 604px;
  }
  .banner__footer {
    position: absolute;
    left: 0;
    right: 0;
    top: 524px;
    height: 80px;
    display: flex;
    align-items: center;
    font-family: "Open Sans", Arial, sans-serif;
    font-weight: 700;
    color: var(--text-white);
  }
  .banner__brand {
    position: absolute;
    left: 38px;
    font-size: 30px;
    letter-spacing: 0.5px;
  }
  .banner__family {
    position: absolute;
    left: 420px;
    font-size: 36px;
    letter-spacing: 0.5px;
    white-space: nowrap;
  }
</style>
</head>
<body>
  <div class="banner">
    <div class="banner__photo" role="img" aria-label="Soft faded photo of two people sharing a warm embrace"></div>

    <h1 class="banner__title">
      <span class="banner__title-word">Keep</span>
      <span class="banner__title-word banner__title-word--accent">Hope</span>
      <span class="banner__title-word">Rising</span>
    </h1>

    <svg class="banner__wave" viewBox="0 0 1200 604" aria-hidden="true">
      <defs>
        <linearGradient id="wave-fill" x1="0" y1="0" x2="0" y2="1">
          <stop offset="0" stop-color="var(--band-grey)"/>
          <stop offset="0.35" stop-color="var(--band-black)"/>
          <stop offset="1" stop-color="var(--band-black)"/>
        </linearGradient>
        <radialGradient id="wave-glow" cx="0.5" cy="0.5" r="0.5">
          <stop offset="0" stop-color="#ffffff"/>
          <stop offset="0.55" stop-color="#ffffff" stop-opacity="0.9"/>
          <stop offset="1" stop-color="#ffffff" stop-opacity="0"/>
        </radialGradient>
      </defs>
      <path d="M0,530 C300,522 600,420 900,414 C1050,411 1150,417 1200,422 L1200,604 L0,604 Z" fill="url(#wave-fill)"/>
      <ellipse cx="826" cy="452" rx="134" ry="24" fill="url(#wave-glow)"/>
    </svg>

    <div class="banner__footer">
      <span class="banner__brand">Harvest Glow TV</span>
      <span class="banner__family">FROM HARVEST GLOW TV FAMILY</span>
    </div>
  </div>
</body>
</html>
```